Safety Brochure for Industry Assocations

This is an 8.5 x 11 single sided brochure for our Occupational Health and Safety Data Analytics software. If you need to use stock images we will pay for them.

Please incorporate our logo and some of the images. No need to incorporate them all. We like the idea of the boots being at the bottom of the page but we're open to other ideas.

Please note that we intend to mail this brochure to different industries so it should be generic (i.e. not construction specific).

Target Market(s)

Safety and Industry Organisations for construction, mining, forestry and oil and gas industries.

Industry/Entity Type

Industry

Font styles to use
Sans Serif

Colors

Designer to choose colors to be used in the design.

Requirements
Must have
• We are a software company that produces safety software. Our customers are companies that engage in dangerous work and use our software to improve their worker's safety. The look and feel should convey the fact that:
• -We are Big Data
• -We are Software
• -We service industry
Nice to have
• Please see the Pixlore photo of the boots. We were hoping that the desiger would be able ti modify the image with an overlay of 0's and 1's in a kind of "matrix" fashion to indicate that we are merging traditional labour work with software.
Should not have
• No medical symbols. Note that WE ARE NOT HEALTH CARE.

```html
<!DOCTYPE html>
<html lang="en">
<head>
<meta charset="utf-8">
<title>Vantrix Analytics – Safety Data Brochure</title>
<link rel="stylesheet" href="https://fonts.googleapis.com/css2?family=Bebas+Neue&family=Arimo:wght@400;700&family=Nunito:wght@900&display=swap">
<style>
  :root{
    --green:#129d4a;
    --lime:#a5cd39;
    --charcoal:#474343;
    --ink:#111111;
    --frame:#000000;
    --paper:#ffffff;
    --logo-grey:#4a4a4a;
  }
  *{margin:0;padding:0;box-sizing:border-box}
  html,body{width:999px;height:1200px;overflow:hidden;background:var(--frame)}
  .canvas{position:relative;width:999px;height:1200px;background:var(--frame)}
  .brochure{position:absolute;left:65px;top:38px;width:869px;height:1124px;background:var(--paper);overflow:hidden;font-family:"Arimo",Arial,sans-serif}
  .shapes{position:absolute;left:0;top:0}
  .abs{position:absolute}

  .headline{left:33px;top:42px;color:var(--paper);font-family:"Bebas Neue",Impact,sans-serif;line-height:.92}
  .headline .line-small{display:block;font-size:58px;letter-spacing:.5px}
  .headline .line-big{display:block;font-size:86px;letter-spacing:1px}

  .brand{left:600px;top:72px;display:flex;align-items:center;gap:12px;color:var(--logo-grey);font-family:"Arimo",Arial,sans-serif;font-weight:700;font-size:24px;line-height:1.05;letter-spacing:1px}
  .brand-dot{width:56px;height:56px;border-radius:50%;background:var(--green);flex:none}

  .pillar-tag{color:var(--paper);font-weight:700;font-size:19px;letter-spacing:.5px}
  .pillar-text{left:37px;color:var(--paper);font-weight:700;font-size:20px;line-height:24px;width:440px}

  .hub{left:383px;top:502px;width:98px;height:98px;border-radius:50%;border:13px solid var(--green);background:var(--paper);display:flex;align-items:center;justify-content:center;text-align:center;font-weight:700;font-size:15px;line-height:20px;color:var(--ink)}

  .boots-photo{left:375px;top:842px;width:480px;height:190px;background:radial-gradient(ellipse at 55% 55%,#5d4534 0%,#7a5d45 32%,#c9bcb0 62%,rgba(255,255,255,0) 80%)}

  .branch{width:300px;text-align:center}
  .branch-icon{display:block;margin:0 auto;width:78px;height:78px}
  .branch-title{margin-top:6px;font-family:"Nunito",Arial,sans-serif;font-weight:900;font-size:23.5px;color:var(--green);letter-spacing:.5px;line-height:26px}
  .branch-text{font-weight:700;font-size:16.5px;line-height:21px;color:var(--ink)}
  .branch-result{position:absolute;left:0;width:100%;top:178px;font-weight:700;font-size:19.5px;color:var(--lime)}

  .tagline{left:43px;top:882px;color:var(--green);font-weight:700;font-size:34px;line-height:41px}

  .site{left:35px;top:1062px;color:var(--paper);font-size:20px}
  .phone{left:422px;top:1050px;color:var(--paper);font-weight:700;font-size:41px;letter-spacing:.5px}
</style>
</head>
<body>
<div class="canvas">
  <div class="brochure">
    <svg class="shapes" width="869" height="1124" viewBox="0 0 869 1124">
      <defs>
        <linearGradient id="dataPhoto" x1="0" y1="0" x2="1" y2="1">
          <stop offset="0" stop-color="#c9d3b8"/>
          <stop offset=".45" stop-color="#8a9c86"/>
          <stop offset="1" stop-color="#3c4a45"/>
        </linearGradient>
      </defs>
      <rect x="300" y="170" width="569" height="314" fill="url(#dataPhoto)" role="img" aria-label="Hand touching a transparent screen showing data charts and a world map"/>
      <polygon points="0,30 555,30 496,170 0,170" fill="var(--green)"/>
      <polygon points="0,170 496,170 364,484 0,484" fill="var(--charcoal)"/>
      <polygon points="562,30 574,30 380,484 368,484" fill="var(--lime)"/>

      <polygon points="0,182 124,182 110,214 0,214" fill="var(--green)"/>
      <polygon points="0,247 157,247 143,279 0,279" fill="var(--green)"/>
      <polygon points="0,334 160,334 146,364 0,364" fill="var(--green)"/>
      <polygon points="0,420 122,420 108,450 0,450" fill="var(--green)"/>

      <path d="M135 637 V612 H725 V637 M432 600 V612" fill="none" stroke="var(--charcoal)" stroke-width="3"/>

      <rect x="0" y="1039" width="869" height="85" fill="var(--charcoal)"/>
      <polygon points="315,1039 869,1039 869,1124 280,1124" fill="var(--green)"/>
    </svg>

    <h1 class="abs headline"><span class="line-small">Leverage the power of</span><span class="line-big">Industry Data!</span></h1>

    <div class="abs brand"><span class="brand-dot"></span><span>Vantrix<br>Analytics</span></div>

    <span class="abs pillar-tag" style="left:38px;top:188px">LEAD</span>
    <p class="abs pillar-text" style="top:220px">the next wave of injury reduction</p>
    <span class="abs pillar-tag" style="left:38px;top:252px">ENGAGE</span>
    <p class="abs pillar-text" style="top:282px">with members through collaboration and<br>benchmarking</p>
    <span class="abs pillar-tag" style="left:38px;top:338px">ANALYZE</span>
    <p class="abs pillar-text" style="top:370px">Accurate, Timely and Complete<br>Leading Indicators</p>
    <span class="abs pillar-tag" style="left:33px;top:425px">TRAIN</span>
    <p class="abs pillar-text" style="left:33px;top:451px">industry more proactively</p>

    <div class="abs hub">EHS<br>DATA</div>

    <div class="abs boots-photo" role="img" aria-label="Pair of worn leather work boots standing on soil"></div>

    <div class="abs branch" style="left:-12px;top:635px">
      <svg class="branch-icon" viewBox="0 0 78 78">
        <circle cx="39" cy="39" r="38" fill="var(--lime)"/>
        <rect x="22" y="24" width="34" height="24" fill="none" stroke="#fff" stroke-width="3"/>
        <path d="M28 42 L36 34 L42 38 L50 29 M39 48 V58 M32 58 H46" fill="none" stroke="#fff" stroke-width="3"/>
      </svg>
      <div class="branch-title">TRAINING</div>
      <p class="branch-text">Analyze needs of Industry<br>Deliver Proactive Training</p>
      <div class="branch-result">Improve Safety</div>
    </div>

    <div class="abs branch" style="left:282px;top:635px">
      <svg class="branch-icon" viewBox="0 0 78 78">
        <circle cx="39" cy="39" r="38" fill="var(--lime)"/>
        <rect x="20" y="24" width="38" height="26" fill="none" stroke="#fff" stroke-width="3"/>
        <circle cx="48" cy="37" r="6" fill="#fff"/>
        <path d="M26 32 H38 M26 38 H38 M26 44 H36 M39 50 V58 M32 58 H46" stroke="#fff" stroke-width="3"/>
      </svg>
      <div class="branch-title">BENCHMARKING</div>
      <p class="branch-text">Engage with Members<br>Promote Collaborative<br>Advancement of Safety</p>
      <div class="branch-result">Improve Safety</div>
    </div>

    <div class="abs branch" style="left:575px;top:635px">
      <svg class="branch-icon" viewBox="0 0 78 78">
        <circle cx="39" cy="39" r="38" fill="var(--lime)"/>
        <path d="M18 22 V54 H60" fill="none" stroke="#fff" stroke-width="3"/>
        <rect x="24" y="42" width="6" height="10" fill="#fff"/>
        <rect x="33" y="38" width="6" height="14" fill="#fff"/>
        <rect x="42" y="40" width="6" height="12" fill="#fff"/>
        <rect x="51" y="33" width="6" height="19" fill="#fff"/>
        <path d="M22 36 L32 30 L42 34 L55 24 M50 23 H56 V29" fill="none" stroke="#fff" stroke-width="2.5"/>
      </svg>
      <div class="branch-title">TREND ANALYSIS</div>
      <p class="branch-text">Monitor Industry Trends<br>Implement Corrective<br>Initiatives</p>
      <div class="branch-result">Improve Safety</div>
    </div>

    <p class="abs tagline">The next BIG STEP<br>in injury redcution for<br>your entire industry.</p>

    <span class="abs site">www.vantrixanalytics.com</span>
    <span class="abs phone">1-888-555-0147</span>
  </div>
</div>
</body>
</html>
```